70th Brenwick Gallery Gala Event postcard

We are looking at a design that uses the word "Evolutionary" - - then the tagline Color, Culture, Creativity. 70th Anniversary Platinum EventI was thinking of the old car ads that talk about the new car coming out next year as Evolutionary in design.. We are having and event to raise money for a new art gallery - in a way this is a new and improved gallery. This is also our "platinum" year. My first thought it that this would be Platinum/ chrome ink on black background. .. It does not have to be a car, but maybe have the look of a car fin. Possibly incorporate red or purple. We have a logo that is different shades of orange, but I can see this being different shades of another color - or chrome. The car fin photos are not mine.. they are mainly for style ideas.. Not to be used in the final design. - i made up a quick idea of my own.. but not good at creating the chrome looking effect. Also not really enough line on mine.

Requirements
Must have
• Logo - but preferably not orange.. would like shades of chrome if possible
• Words in metallic. 4X6 postcard.
Should not have
• Actual car photos - those were borrowed

```html
<!DOCTYPE html>
<html lang="en">
<head>
<meta charset="utf-8">
<title>70th Brenwick Gallery Gala Event</title>
<link rel="stylesheet" href="https://fonts.googleapis.com/css2?family=Oswald:wght@400;500&family=Roboto:wght@400&display=swap">
<style>
  :root {
    --ink-black: #000000;
    --chrome-light: #f4f4f4;
    --chrome-mid: #b9b9b9;
    --chrome-dark: #6d6d6d;
    --chrome-shadow: #2a2a2a;
    --band-text: #1a1a1a;
    --tagline: #ffffff;
    --taillight-red: #d41f26;
  }
  html, body {
    margin: 0;
    padding: 0;
    overflow: hidden;
    background: var(--ink-black);
  }
  .postcard {
    position: relative;
    width: 800px;
    height: 1200px;
    background: var(--ink-black);
    overflow: hidden;
  }
  .guild-mark {
    position: absolute;
    top: 130px;
    left: 0;
    width: 800px;
    display: flex;
    justify-content: center;
    align-items: center;
    gap: 20px;
  }
  .guild-mark__dot {
    width: 100px;
    height: 100px;
    border-radius: 50%;
    background: var(--chrome-mid);
  }
  .guild-mark__name {
    font-family: "Oswald", sans-serif;
    font-weight: 500;
    color: var(--chrome-light);
    text-transform: uppercase;
    line-height: 1;
    margin: 0;
  }
  .guild-mark__name span {
    display: block;
  }
  .guild-mark__primary {
    font-size: 58px;
    letter-spacing: 5px;
  }
  .guild-mark__secondary {
    font-size: 24px;
    letter-spacing: 3px;
    margin-top: 6px;
  }
  .headline-band {
    position: absolute;
    top: 343px;
    left: 68px;
    width: 660px;
    height: 109px;
    background: linear-gradient(90deg, var(--chrome-dark) 0%, var(--chrome-light) 30%, var(--chrome-mid) 55%, var(--chrome-light) 78%, var(--chrome-dark) 100%);
    display: flex;
    align-items: center;
    justify-content: center;
  }
  .headline-band__title {
    margin: 0;
    font-family: "Oswald", sans-serif;
    font-weight: 400;
    font-size: 80px;
    letter-spacing: 11px;
    padding-left: 11px;
    color: var(--band-text);
    text-transform: uppercase;
    line-height: 1;
  }
  .tagline {
    position: absolute;
    top: 482px;
    left: 0;
    width: 800px;
    margin: 0;
    text-align: center;
    font-family: "Roboto", sans-serif;
    font-weight: 400;
    font-size: 38px;
    letter-spacing: 5px;
    line-height: 1.2;
    color: var(--tagline);
    text-transform: uppercase;
  }
  .fin-artwork {
    position: absolute;
    top: 620px;
    left: 0;
    width: 800px;
    height: 520px;
    background:
      radial-gradient(circle at 545px 405px, var(--taillight-red) 0, var(--taillight-red) 48px, rgba(212, 31, 38, 0) 80px),
      radial-gradient(ellipse 300px 170px at 330px 230px, rgba(244, 244, 244, 0.75) 0%, rgba(185, 185, 185, 0.35) 55%, rgba(0, 0, 0, 0) 100%),
      linear-gradient(160deg, var(--ink-black) 0%, var(--chrome-shadow) 22%, var(--chrome-mid) 42%, var(--chrome-dark) 58%, var(--chrome-shadow) 74%, var(--ink-black) 92%);
  }
</style>
</head>
<body>
  <main class="postcard">
    <header class="guild-mark">
      <div class="guild-mark__dot"></div>
      <p class="guild-mark__name">
        <span class="guild-mark__primary">Brenwick</span>
        <span class="guild-mark__secondary">Gallery Guild</span>
      </p>
    </header>
    <div class="headline-band">
      <h1 class="headline-band__title">Evolutionary</h1>
    </div>
    <p class="tagline">Color, Culture, Creativity</p>
    <div class="fin-artwork" role="img" aria-label="Chrome-styled black and white illustration of a classic car tail fin with script badge and a red tail light"></div>
  </main>
</body>
</html>
```